Design few pages for professional development app

I need a website design for a prototype project. The goal of the project is to prototype a few basic screens for a professional development application.

The final design should be clean, modern, and appeal to a professional millenial clientele.The designs have been wireframed (see attached), and we'd like these wireframes converted to design files.

Here is the list of goals and tasks that correspond to the design: https://sheets.plorvane.com/grid/d/7kQWm48p3XZvrt2bYH5LcNaeJoTsUDfi82GhKxMp/edit?view=shared

Number of Pages Required

5+ page

Font styles to use
Serif
Sans Serif

Colors

Designer to choose colors to be used in the design.

Requirements
Nice to have
• Uses Google Material Design, Bootstrap, or another framework

```html
<!DOCTYPE html>
<html lang="en">
<head>
<meta charset="utf-8">
<title>Ascendly — Take Control of your Career</title>
<link rel="stylesheet" href="https://fonts.googleapis.com/css2?family=Noto+Sans:wght@400;600;700&display=swap">
<style>
  :root {
    --sky: #f2f7fc;
    --cloud: #ffffff;
    --navy: #0d4a80;
    --ink: #333a40;
    --brand-blue: #2196f3;
    --link-blue: #1e88e5;
    --grass: #86bc00;
    --grass-deep: #72a800;
    --card: #f7fafd;
    --avatar: #b9c9d6;
    --scene-left: #d6e6f4;
    --scene-right: #e2eef8;
  }
  * { box-sizing: border-box; margin: 0; padding: 0; }
  html, body { width: 1200px; height: 701px; overflow: hidden; }
  body {
    font-family: "Noto Sans", sans-serif;
    background: var(--sky);
    color: var(--ink);
    position: relative;
  }
  .backdrop { position: absolute; inset: 0; }
  .site-header { position: absolute; top: 0; left: 0; right: 0; height: 80px; }
  .brand {
    position: absolute; left: 43px; top: 48px;
    display: flex; align-items: center; gap: 7px;
    font-size: 15px; font-weight: 600; color: var(--ink);
  }
  .brand-dot { width: 12px; height: 12px; border-radius: 50%; background: var(--grass-deep); }
  .header-actions {
    position: absolute; right: 48px; top: 29px;
    display: flex; align-items: center; gap: 14px;
  }
  .header-divider { width: 1px; height: 14px; background: #c5d3df; }
  .login { color: var(--link-blue); font-size: 11px; font-weight: 600; text-decoration: none; }
  .hero { position: absolute; top: 114px; left: 0; right: 0; text-align: center; }
  .hero-title {
    font-size: 40px; font-weight: 600; color: var(--navy);
    letter-spacing: -0.4px; line-height: 1.2;
  }
  .hero-lead { margin-top: 18px; font-size: 14px; line-height: 23px; color: var(--ink); }
  .cta {
    display: inline-block; margin-top: 24px;
    width: 163px; height: 37px; line-height: 37px;
    background: var(--brand-blue); color: #fff;
    font-size: 11px; font-weight: 600; text-decoration: none; border-radius: 2px;
  }
  .testimonial {
    position: absolute; top: 334px; width: 279px; height: 116px;
    background: var(--card);
    box-shadow: 0 4px 18px rgba(120, 150, 180, 0.12);
    display: flex; align-items: flex-start; padding: 32px 0 0 18px; gap: 20px;
  }
  .testimonial.first { left: 312px; }
  .testimonial.second { left: 609px; }
  .avatar {
    flex: none; width: 50px; height: 50px; border-radius: 50%;
    background: linear-gradient(160deg, #c9d8e4, var(--avatar));
  }
  .quote { font-size: 11px; line-height: 18px; color: var(--ink); }
  .author { font-weight: 700; display: block; }
  .scene-runner {
    position: absolute; left: 20px; top: 352px; width: 320px; height: 270px;
    background: linear-gradient(160deg, var(--scene-left), rgba(214, 230, 244, 0.4));
    border-radius: 24px 24px 0 0;
  }
  .scene-city {
    position: absolute; left: 780px; top: 380px; width: 410px; height: 242px;
    background: linear-gradient(180deg, rgba(226, 238, 248, 0.5), var(--scene-right));
    border-radius: 24px 24px 0 0;
  }
</style>
</head>
<body>
  <svg class="backdrop" width="1200" height="701" viewBox="0 0 1200 701" aria-hidden="true">
    <path d="M0 0 H150 Q170 30 160 60 Q150 78 110 80 Q40 85 15 130 Q-5 175 15 220 Q40 265 100 265 Q170 270 190 320 Q205 360 190 400 L0 420 Z" fill="var(--cloud)" opacity="0.75"/>
    <path d="M1200 120 Q1170 160 1110 165 Q1060 175 1070 235 Q1080 290 1140 300 L1200 310 Z" fill="var(--cloud)" opacity="0.8"/>
    <rect x="0" y="622" width="1200" height="79" fill="var(--grass)"/>
    <path d="M0 650 Q20 622 60 622 L0 622 Z" fill="var(--sky)"/>
    <rect x="130" y="622" width="1038" height="61" rx="30" fill="var(--grass-deep)"/>
  </svg>

  <div class="scene-runner" role="img" aria-label="Illustration of a businessman in a blue suit running with a briefcase over a rising trend arrow, with a shrub"></div>
  <div class="scene-city" role="img" aria-label="Illustration of a pale blue city skyline with a shrub"></div>

  <header class="site-header">
    <div class="brand"><span class="brand-dot"></span>Ascendly</div>
    <nav class="header-actions">
      <svg width="12" height="12" viewBox="0 0 12 12" aria-label="Search" role="img">
        <circle cx="5" cy="5" r="3.8" fill="none" stroke="var(--link-blue)" stroke-width="1.8"/>
        <line x1="7.8" y1="7.8" x2="11" y2="11" stroke="var(--link-blue)" stroke-width="1.8" stroke-linecap="round"/>
      </svg>
      <span class="header-divider"></span>
      <a class="login" href="#">Log In</a>
    </nav>
  </header>

  <main class="hero">
    <h1 class="hero-title">Take Control of your Career</h1>
    <p class="hero-lead">Complete short, actionable tasks guaranteed to get you further in your career, faster than ever.<br>Ready to get started? Take the short quiz below and get your personalized path today.</p>
    <a class="cta" href="#">Get Started</a>
  </main>

  <section class="testimonial first">
    <div class="avatar" role="img" aria-label="Portrait photo of Lena Moretti"></div>
    <p class="quote">I love how quickly I can do the<br>tasks,and see progress<span class="author">Lena Moretti</span></p>
  </section>
  <section class="testimonial second">
    <div class="avatar" role="img" aria-label="Portrait photo of Tom Hadley"></div>
    <p class="quote">The best investment I've made in<br>myself in ages.<span class="author">Tom Hadley</span></p>
  </section>
</body>
</html>
```